Fahrzeugbeschriftung für Elektrofirma
Zielgruppe
Wir sind eine Elektrofirma und suchen ein hochwertiges Design, unsere Ziehlgruppe sind smarthome bewuste Familen oder Männner.
Aufgabenstellung
Wir haben varelle Toriv L1 H2 und vastrano L1 H2,
So ähnlich wie bei Lutz & Baier
Hinten: - Gebäudetechnik , - Smarthome, - Sicherheitstechnik,
Telefonnummer 02087 3519284
Facebook: ElektroTannreuter
Instagram: elektro_tannreuter
Seiten: Ahornweg 17
47128 Dinslaken
Seiten hinten: Logo mit Tannreuter Elektro- und Datentechnik
www.elektro-tannreuter-beispiel.de, info@elektro-tannreuter-beispiel.de
keine komplett Folierung

```html
<!DOCTYPE html>
<html lang="de">
<head>
<meta charset="utf-8">
<title>Tannreuter – Heckbeschriftung</title>
<link rel="stylesheet" href="https://fonts.googleapis.com/css2?family=Fira+Sans+Condensed:wght@500&display=swap">
<style>
  :root {
    --navy: #1f3a5f;
    --navy-ink: #24344d;
    --teal: #17aab9;
    --white: #ffffff;
    --backdrop: #e6e9ec;
    --text-light: #f2f5f8;
  }
  html, body {
    margin: 0;
    padding: 0;
    width: 1200px;
    height: 1169px;
    overflow: hidden;
    background: var(--backdrop);
  }
  .canvas {
    position: relative;
    width: 1200px;
    height: 1169px;
  }
  .rear-panel {
    position: absolute;
    left: 100px;
    top: 200px;
    width: 1000px;
    height: 770px;
    border-radius: 40px 40px 12px 12px;
    overflow: hidden;
    background: var(--white);
    box-shadow: 0 2px 10px rgba(0,0,0,0.08);
  }
  .roof-band {
    position: absolute;
    left: 0; top: 0;
    width: 100%;
    height: 46px;
    background: var(--teal);
  }
  .lower-band {
    position: absolute;
    left: 0; top: 355px;
    width: 100%;
    height: 415px;
    background: var(--navy);
  }
  .panel-seam {
    position: absolute;
    left: 499px;
    top: 0;
    width: 2px;
    height: 100%;
    background: rgba(0,0,0,0.10);
  }
  .brand {
    position: absolute;
    left: 150px;
    top: 150px;
    display: flex;
    align-items: center;
    gap: 24px;
  }
  .brand-mark {
    flex: none;
    width: 72px;
    height: 72px;
    background: var(--teal);
  }
  .brand-name {
    font-family: "Fira Sans Condensed", sans-serif;
    font-weight: 500;
    font-size: 44px;
    line-height: 1;
    color: var(--navy-ink);
    white-space: nowrap;
  }
  .services {
    position: absolute;
    left: 552px;
    top: 380px;
    margin: 0;
    padding: 0;
    list-style: none;
    font-family: "Fira Sans Condensed", sans-serif;
    font-weight: 500;
    font-size: 28px;
    color: var(--text-light);
  }
  .services li { line-height: 44px; }
  .services li::before { content: "- "; }
  .contact {
    position: absolute;
    left: 550px;
    top: 640px;
    font-family: "Fira Sans Condensed", sans-serif;
    font-weight: 500;
    color: var(--text-light);
  }
  .contact-row {
    display: flex;
    align-items: center;
    gap: 14px;
  }
  .contact-phone { font-size: 40px; }
  .contact-web { font-size: 23px; margin-top: 16px; }
  .contact-icon { flex: none; }
  .social {
    position: absolute;
    left: 152px;
    top: 680px;
    font-family: "Fira Sans Condensed", sans-serif;
    font-weight: 500;
    font-size: 25px;
    color: var(--text-light);
  }
  .social-row {
    display: flex;
    align-items: center;
    gap: 12px;
    line-height: 44px;
  }
  .social-dot {
    width: 26px;
    height: 26px;
    border-radius: 6px;
    background: var(--text-light);
  }
</style>
</head>
<body>
<div class="canvas">
  <div class="rear-panel">
    <div class="roof-band"></div>
    <div class="lower-band"></div>
    <div class="panel-seam"></div>

    <div class="brand">
      <div class="brand-mark"></div>
      <span class="brand-name">Tannreuter Elektro- und Datentechnik</span>
    </div>

    <ul class="services">
      <li>Gebäudetechnik</li>
      <li>Smarthome</li>
      <li>Sicherheitstechnik</li>
    </ul>

    <div class="contact">
      <div class="contact-row contact-phone">
        <svg class="contact-icon" width="36" height="36" viewBox="0 0 36 36" aria-hidden="true">
          <circle cx="18" cy="18" r="17" fill="#f2f5f8"/>
          <path d="M12.5 9.5c1-.6 2-.3 2.6.6l1.6 2.6c.5.9.3 1.9-.5 2.5l-1.2.9c.9 2.2 2.6 3.9 4.8 4.8l.9-1.2c.6-.8 1.6-1 2.5-.5l2.6 1.6c.9.6 1.2 1.6.6 2.6l-.9 1.4c-.7 1.1-2 1.6-3.300 1.3-5.3-1.3-9.5-5.5-10.8-10.8-.3-1.3.2-2.6 1.3-3.3z" fill="#1f3a5f"/>
        </svg>
        <span>02087/3519284</span>
      </div>
      <div class="contact-row contact-web">
        <svg class="contact-icon" width="34" height="34" viewBox="0 0 34 34" aria-hidden="true">
          <circle cx="17" cy="17" r="15" fill="none" stroke="#f2f5f8" stroke-width="2.5"/>
          <ellipse cx="17" cy="17" rx="6.5" ry="15" fill="none" stroke="#f2f5f8" stroke-width="2"/>
          <line x1="2" y1="17" x2="32" y2="17" stroke="#f2f5f8" stroke-width="2"/>
        </svg>
        <span>www.elektro-tannreuter-beispiel.de</span>
      </div>
    </div>

    <div class="social">
      <div class="social-row"><span class="social-dot"></span><span>ElektroTannreuter</span></div>
      <div class="social-row"><span class="social-dot"></span><span>elektro_tannreuter</span></div>
    </div>
  </div>
</div>
</body>
</html>
```